PowerPoint Template Needed for Investment Firm

Norvelle Capital Management is an emerging wealth management firm based in New Jersey. It offers superior investment returns to high net worth individuals and institutions by finding undervalued assets.

We recently selected a company logo which was inspired by the Tucana constellation. Beta Tucanae is a group of six stars, containing star cluster 47 Tucanae, rated the second brightest object in the sky.

Now we need a PowerPoint template with the designs for the following:

1. Title/cover page slide
2. Content slide with title
3. Section slide - to introduce a new section
4. Final slide - with contact information

The slides will be used at investor presentations, that is, to provide information about the company to potential investors. Since we are an investment firm, the design should project a sense of stability, growth and professionalism. The owner is interested in something simple yet striking, which of course is consistent with the logo. I'm thinking more conservative colors and Sans Serif fonts.

I plan on changing the status to non-refundable once I see some designs that I really like.

Target Market(s)

Wealthy individuals, probably middle aged or older, in the US

Industry/Entity Type

Conservative

Requirements
Must have
• Sans serif fonts
Clean, very professional look
Conservative colors that complement existing logo
Should not have
• Anything too busy or complicated

```html
<!DOCTYPE html>
<html lang="en">
<head>
<meta charset="utf-8">
<title>Norvelle Capital Management – Slide Template</title>
<link rel="stylesheet" href="https://fonts.googleapis.com/css2?family=Arimo:wght@400;700&family=Open+Sans:wght@400&display=swap">
<style>
  :root {
    --frame: #939598;
    --paper: #e6e7e8;
    --charcoal: #3a3838;
    --ink: #2f2f2f;
    --navy-text: #2e3a78;
    --blue-core: #1d42b4;
    --blue-edge: #222429;
    --mark: #1f3a9e;
    --white: #ffffff;
    --pie-yellow: #fff03c;
    --pie-green: #41a85a;
    --pie-red: #d13437;
    --pie-blue: #0db0ea;
    --pie-shadow: #a6a7a9;
  }
  * { margin: 0; padding: 0; box-sizing: border-box; }
  html, body { width: 1200px; height: 938px; overflow: hidden; background: var(--frame); }
  .deck { position: relative; width: 1200px; height: 938px; font-family: "Arimo", Arial, sans-serif; }
  .slide { position: absolute; width: 577px; height: 446px; background: var(--paper); overflow: hidden; }
  .slide--cover { left: 17px; top: 17px; }
  .slide--section { left: 604px; top: 17px; }
  .slide--content { left: 17px; top: 472px; }
  .slide--closing { left: 604px; top: 472px; }

  .blue-band { position: absolute; background: radial-gradient(ellipse 45% 140% at 50% 50%, var(--blue-core) 0%, #17307e 45%, var(--blue-edge) 100%); }

  .side-column { position: absolute; left: 0; top: 0; width: 155px; height: 365px; background: var(--charcoal); }

  .brand { position: absolute; display: flex; flex-direction: column; align-items: center; }
  .brand__square { width: 36px; height: 36px; background: var(--mark); border-radius: 4px; }
  .brand__name { margin-top: 6px; font-family: "Open Sans", Arial, sans-serif; font-size: 8.5px; color: var(--ink); white-space: nowrap; }
  .brand--footer { left: 0; top: 378px; width: 155px; }
  .brand--small { left: 0; top: 5px; width: 61px; }
  .brand--small .brand__square { width: 18px; height: 18px; border-radius: 2px; }
  .brand--small .brand__name { margin-top: 3px; font-size: 4.5px; }

  .cover-title { position: absolute; left: 196px; top: 266px; color: var(--ink); font-weight: 700; }
  .cover-title__main { font-size: 31px; line-height: 34px; }
  .cover-title__sub { font-size: 23px; line-height: 30px; }
  .web-address { position: absolute; left: 169px; top: 424px; font-family: "Open Sans", Arial, sans-serif; font-size: 9.5px; color: var(--white); }

  .section-title { position: absolute; right: 58px; top: 245px; text-align: right; font-size: 24px; line-height: 29px; font-weight: 700; color: var(--ink); }
  .section-intro { position: absolute; right: 58px; top: 313px; text-align: right; font-family: "Open Sans", Arial, sans-serif; font-size: 10px; line-height: 14px; color: var(--navy-text); }

  .content-title { position: absolute; left: 61px; top: 82px; width: 468px; font-size: 16px; font-weight: 700; color: var(--ink); border-bottom: 1px solid var(--ink); padding-bottom: 0; line-height: 18px; }
  .content-title span { background: var(--paper); padding-right: 2px; }
  .bullets { position: absolute; left: 72px; top: 144px; font-family: "Open Sans", Arial, sans-serif; font-size: 10px; line-height: 14px; color: var(--navy-text); list-style: none; }
  .bullets li::before { content: "•"; margin-right: 6px; }
  .bullets li.gap { margin-top: 14px; }
  .pie { position: absolute; left: 305px; top: 154px; }

  .closing-band { position: absolute; left: 0; top: 364px; width: 577px; height: 82px; background: var(--charcoal); }
  .contact-line { position: absolute; left: 0; top: 378px; width: 577px; text-align: center; font-family: "Open Sans", Arial, sans-serif; font-size: 9.5px; color: var(--white); }
</style>
</head>
<body>
<main class="deck">

  <section class="slide slide--cover">
    <div class="side-column"></div>
    <h1 class="cover-title">
      <div class="cover-title__main">Norvelle</div>
      <div class="cover-title__sub">Capital Management</div>
    </h1>
    <div class="blue-band" style="left:155px; top:365px; width:422px; height:81px;"></div>
    <div class="brand brand--footer">
      <div class="brand__square"></div>
      <div class="brand__name">Norvelle Capital Management</div>
    </div>
    <p class="web-address">www.norvellecapital.com</p>
  </section>

  <section class="slide slide--section">
    <h2 class="section-title">Legal<br>Disclaimers</h2>
    <p class="section-intro">Lorem ipsum dolor sit amet, consectetur adipiscing elit.<br>Aenean nec odio nisi, aliquet molestie est.</p>
    <div class="blue-band" style="left:155px; top:365px; width:422px; height:81px;"></div>
    <div class="brand brand--footer">
      <div class="brand__square"></div>
      <div class="brand__name">Norvelle Capital Management</div>
    </div>
  </section>

  <section class="slide slide--content">
    <div class="blue-band" style="left:61px; top:0; width:516px; height:41px;"></div>
    <div class="brand brand--small">
      <div class="brand__square"></div>
      <div class="brand__name">Norvelle Capital Management</div>
    </div>
    <h2 class="content-title"><span>Financial Returns</span></h2>
    <ul class="bullets">
      <li>Lorem ipsum dolor sit amet, consectetur adipiscing elit.</li>
      <li>Aenean nec odio nisi, aliquet molestie est.</li>
      <li>Cras sed purus a libero malesuada facilisis.</li>
      <li class="gap">Sed eget ipsum felis, nec euismod purus.</li>
      <li>Fusce a purus nisl, a facilisis augue.</li>
    </ul>
    <svg class="pie" width="232" height="232" viewBox="-116 -116 232 232" role="img" aria-label="Pie chart of financial returns">
      <circle cx="3" cy="5" r="108" fill="var(--pie-shadow)"/>
      <path d="M0 0 L-38.7 -100.8 A108 108 0 0 1 73.7 -79 Z" fill="var(--pie-yellow)"/>
      <path d="M0 0 L73.7 -79 A108 108 0 0 1 101.5 36.9 Z" fill="var(--pie-green)"/>
      <path d="M0 0 L101.5 36.9 A108 108 0 0 1 77.7 75 Z" fill="var(--white)"/>
      <path d="M0 0 L77.7 75 A108 108 0 0 1 -107.9 -3.8 Z" fill="var(--pie-red)"/>
      <path d="M0 0 L-107.9 -3.8 A108 108 0 0 1 -38.7 -100.8 Z" fill="var(--pie-blue)"/>
    </svg>
  </section>

  <section class="slide slide--closing">
    <div class="closing-band"></div>
    <p class="contact-line">48 Harbor Ave. Newark, NJ 07102 | www.norvellecapital.com | jcarter@norvellecapital.com</p>
  </section>

</main>
</body>
</html>
```